Topics to Raise With a Clinician tri-fold brochure

We are looking for a 1 page (front and back) 8.5" x 11" tri-fold brochure. Please refer back to our Rack Cards for a similar look and feel to the design. They can be found here: https://otvenrix.org/resources/sunny-garden-steady-mind-rack-card-series/.
This brochure is titled: Topics to Raise With a Clinician on Forgetfulness.

The document is for older readers. Do not put text over graphics and keep it simple and easy to read with high contrast.

We want some very simple design element(s) incorporated that convey Native American communities or heritage. But NO headdress, teepee graphics, owls etc. I have included some images, please use your creative discretion to use which ones look good.

Please remember to include the funding statement - it can be in a very small font 6/7 point: For more information about our project, please visit https://otvenrix.org/mind-care/resources - This rack card is supported by the Bureau for Wellness Tracking and Outreach (BWTO) of the Federal Office of Wellbeing and Family Supports (FWF) as part of a financial assistance award totaling $948,260.00 with 100 percent funded by BWTO/FWF. The contents are those of the author(s) and do not necessarily represent the official views of, nor an endorsement, by BWTO/FWF, or the National Civic Administration.

Please feel free to choose one of each of the 2 logos that looks best (horizontal or square). We have the Otvenrix logo and the Cedar Path Learning Hub logo we would like to add. I have added the document and there are images to choose from to use.

I am thinking that the front of the tri-fold should have one of the pictures of a patient and doctor talking. I have included several options. Please use your creative discretion to choose what looks best.

Please let me know if you have any questions, thank you!

```html
<!DOCTYPE html>
<html lang="en">
<head>
<meta charset="utf-8">
<title>Topics to Raise With a Clinician on Forgetfulness – Tri-fold Brochure</title>
<link href="https://fonts.googleapis.com/css2?family=Montserrat:wght@600;700;800&family=Open+Sans:wght@400;600;700&display=swap" rel="stylesheet">
<style>
:root{
  --stage:#b9b9b9;
  --teal:#1f4f57;
  --teal-deep:#173c43;
  --rust:#9b4a39;
  --red:#b8402c;
  --cream:#f5efe4;
  --paper:#ffffff;
  --ink:#2a2a2a;
  --band:#c98a5e;
  --peach:#f4c9a8;
}
*{box-sizing:border-box;margin:0;padding:0}
html,body{width:1200px;height:2360px;overflow:hidden}
body{background:var(--stage);font-family:"Open Sans",Arial,sans-serif;color:var(--ink);position:relative}
.spread{position:absolute;left:20px;width:1160px;height:896px;display:flex;box-shadow:0 6px 18px rgba(0,0,0,.25)}
.spread--outside{top:60px}
.spread--inside{top:1040px;background:var(--rust);color:#fff;flex-direction:column}
.panel{width:386.67px;height:100%;position:relative;overflow:hidden}
h2,h3,.title{font-family:"Montserrat",Arial,sans-serif}
.photo{display:block}
.band{height:18px;background:var(--band);flex:none}

/* outside left */
.panel--tracking{background:var(--cream)}
.tracking-head{background:var(--red);color:#fff;padding:20px 24px 18px}
.tracking-head h2{font-size:26px;font-weight:800}
.tracking-head p{font-size:14px;line-height:1.45;margin-top:8px}
.log{margin:22px 24px;width:calc(100% - 48px);border-collapse:collapse;font-size:12px;background:#fff}
.log th{background:var(--teal);color:#fff;padding:7px 5px;font-weight:700;text-align:left}
.log td{border:1px solid #d7b2a6;height:27px}
.panel--tracking .photo{position:absolute;left:0;bottom:0;width:100%;height:280px;background:linear-gradient(135deg,#dcdcdc,#9fb5bb)}

/* outside middle */
.panel--resources{background:var(--paper)}
.panel--resources .photo{height:240px;background:linear-gradient(160deg,#c7c7c7,#7d8689)}
.resources{background:var(--teal);color:#fff;margin:-30px 20px 0;position:relative;padding:20px 16px 12px}
.resources h2{font-size:22px;font-weight:800;text-align:center;line-height:1.2;margin-bottom:14px}
.link-card{background:#fff;color:var(--teal-deep);padding:8px 10px;margin-bottom:10px;text-align:center;font-size:13px;font-weight:700;line-height:1.35}
.link-card span{display:block;font-weight:600;color:var(--red);font-size:12px}
.funding{position:absolute;left:20px;right:20px;bottom:14px;font-size:8px;line-height:1.4;color:#444}

/* outside right cover */
.panel--cover{background:var(--paper);display:flex;flex-direction:column}
.brand{display:flex;align-items:center;gap:14px;padding:26px 28px 22px}
.brand-mark{width:48px;height:48px;border-radius:50%;background:var(--teal);flex:none}
.brand-name{font-family:"Montserrat",Arial,sans-serif;font-weight:700;color:var(--teal);font-size:17px;line-height:1.25}
.cover-title{background:var(--teal);color:#fff;padding:30px 28px}
.cover-title .title{font-size:40px;font-weight:800;line-height:1.15}
.cover-title .title em{font-style:normal;color:var(--peach)}
.panel--cover .photo{flex:1;background:linear-gradient(150deg,#c8b6a4,#6d7c80)}

/* inside */
.intro{padding:24px 40px 14px;font-size:15px;line-height:1.55}
.inside-row{display:flex;flex:1;min-height:0}
.inside-row .panel{height:auto}
.qa{padding:8px 28px 20px}
.qa h3{font-size:27px;font-weight:800;color:#fff;line-height:1.15;margin:10px 0 12px}
.qa h3.accent{color:var(--peach);margin-top:18px}
.qa ul{list-style:none}
.qa li{font-size:15px;line-height:1.4;padding-left:18px;position:relative;margin-bottom:8px}
.qa li::before{content:"";position:absolute;left:2px;top:8px;width:7px;height:7px;background:var(--peach);border-radius:50%}
.qa ul.sub li{margin-left:18px;font-size:14px}
.panel--couple .photo{margin:16px 24px 0;height:470px;background:linear-gradient(160deg,#b49a86,#6f5a4c)}
.panel--couple .caption{margin:18px 24px;font-size:15px;line-height:1.5}
.panel--asked .photo{margin:14px 0 0;height:190px;background:linear-gradient(90deg,#d1b27b,#6f8f8f,#a55a45)}
</style>
</head>
<body>

<section class="spread spread--outside" aria-label="Brochure outside">
  <div class="panel panel--tracking">
    <div class="tracking-head">
      <h2>Symptom Tracking:</h2>
      <p>By tracking symptoms like forgetfulness, confusion, or difficulty with everyday tasks, individuals and their caregivers can provide accurate information to healthcare providers, leading to better planning and support.</p>
    </div>
    <table class="log">
      <tr><th>Date</th><th>Symptom</th><th>Time</th><th>Notes</th></tr>
      <tr><td></td><td></td><td></td><td></td></tr>
      <tr><td></td><td></td><td></td><td></td></tr>
      <tr><td></td><td></td><td></td><td></td></tr>
      <tr><td></td><td></td><td></td><td></td></tr>
      <tr><td></td><td></td><td></td><td></td></tr>
      <tr><td></td><td></td><td></td><td></td></tr>
      <tr><td></td><td></td><td></td><td></td></tr>
      <tr><td></td><td></td><td></td><td></td></tr>
    </table>
    <div class="photo" role="img" aria-label="Photo of a clinician writing notes on a clipboard"></div>
  </div>

  <div class="panel panel--resources">
    <div class="photo" role="img" aria-label="Photo of an older man looking thoughtful"></div>
    <div class="resources">
      <h2>For More Information About Memory Loss</h2>
      <div class="link-card">10 Signs of Thinking or Memory Changes That Might Be Dementia<span>https://lnk.otvenrix.org/10signs</span></div>
      <div class="link-card">Dementia Friendly Resources<span>https://lnk.otvenrix.org/friendly</span></div>
      <div class="link-card">BWTO Living with Memory Loss<span>https://lnk.otvenrix.org/living</span></div>
      <div class="link-card">Elder Voices Alliance Questions to Ask<span>https://lnk.otvenrix.org/askdoc</span></div>
      <div class="link-card">Pathways to Well-Being with Dementia<span>https://lnk.otvenrix.org/pathways</span></div>
    </div>
    <p class="funding">For more information about our project, please visit https://otvenrix.org/mind-care/resources - This rack card is supported by the Bureau for Wellness Tracking and Outreach (BWTO) of the Federal Office of Wellbeing and Family Supports (FWF) as part of a financial assistance award totaling $948,260.00 with 100 percent funded by BWTO/FWF. The contents are those of the author(s) and do not necessarily represent the official views of, nor an endorsement, by BWTO/FWF, or the National Civic Administration.</p>
  </div>

  <div class="panel panel--cover">
    <div class="band"></div>
    <div class="brand">
      <div class="brand-mark"></div>
      <div class="brand-name">Otvenrix Alliance<br>for Tribal Elders</div>
    </div>
    <div class="cover-title">
      <p class="title">Topics to Raise With a Clinician on <em>Forgetfulness</em></p>
    </div>
    <div class="photo" role="img" aria-label="Photo of a clinician talking with an older patient"></div>
  </div>
</section>

<section class="spread spread--inside" aria-label="Brochure inside">
  <div class="band"></div>
  <p class="intro">If you notice forgetfulness or memory changes in yourself or a loved one, talking to a clinician is an important first step. Memory changes can have many causes, and some of them can be treated. Writing down your questions before a visit helps you get the most from your time together. Bring a family member or friend to take notes, and share any symptoms you have tracked. Together you can plan the next steps for care, support and staying well at home and in the community.</p>
  <div class="inside-row">
    <div class="panel qa">
      <h3>Topics to Raise With a Clinician:</h3>
      <ul>
        <li>What could be causing my memory changes?</li>
        <li>What tests will I need, and what do they show?</li>
        <li>Could a medicine or other condition be a cause?</li>
        <li>How will this change my daily life?</li>
      </ul>
      <ul class="sub">
        <li>Driving and getting around</li>
        <li>Managing money and bills</li>
        <li>Taking medicines safely</li>
      </ul>
      <h3 class="accent">What happens after diagnosis?</h3>
      <ul>
        <li>What treatments are available?</li>
        <li>Are there local support groups?</li>
        <li>Who should I call with new questions?</li>
      </ul>
    </div>
    <div class="panel panel--couple">
      <div class="photo" role="img" aria-label="Photo of an older couple smiling together"></div>
      <p class="caption">Family and community are part of the care journey. Share what you learn with the people who support you.</p>
    </div>
    <div class="panel panel--asked qa">
      <div class="photo" role="img" aria-label="Illustration of three head profiles in warm and teal tones"></div>
      <h3>Questions Your Doctor May Ask You:</h3>
      <ul>
        <li>When did your symptoms of forgetfulness begin?</li>
        <li>What helps you remember things?</li>
        <li>What specific memory issues are you having?</li>
        <li>Have you recently been sick?</li>
        <li>Have you had a fall or head injury?</li>
        <li>Have you been feeling sad or worried?</li>
        <li>Have there been any recent changes in your life?</li>
      </ul>
    </div>
  </div>
  <div class="band"></div>
</section>

</body>
</html>
```